Updated DJ business Card showing other businesses

DJ Kestro offers professional mobile dj services including DJ. MC. Karaoke.
Quietwave Disco (will attach logo)
I also offer a 360 Photo Booth.

Contact info:
(555) 314-7720
lenny.corbitt@mailvane.net
Social Media @DJKestroBPZ

```html
<!DOCTYPE html>
<html lang="en">
<head>
<meta charset="utf-8">
<title>DJ Kestro – Business Card</title>
<link rel="stylesheet" href="https://fonts.googleapis.com/css2?family=Share+Tech+Mono&display=swap">
<style>
  :root {
    --navy: #252b3a;
    --crimson: #d4174a;
    --white: #ffffff;
    --stage: #8c8598;
    --ink: #1c1f27;
  }
  * { box-sizing: border-box; margin: 0; padding: 0; }
  html, body { width: 1200px; height: 1200px; overflow: hidden; }
  body {
    background: var(--stage);
    font-family: "Share Tech Mono", monospace;
    position: relative;
  }
  .card {
    position: absolute;
    width: 708px;
    height: 404px;
    overflow: hidden;
    box-shadow: 10px 12px 18px rgba(0,0,0,0.35);
  }
  .card-front { left: 111px; top: 158px; background: var(--navy); }
  .card-back { left: 364px; top: 619px; background: var(--white); }
  .block { position: absolute; }

  /* Front */
  .front-tab { left: 0; top: 137px; width: 37px; height: 130px; background: var(--crimson); }
  .front-panel { left: 419px; top: 137px; width: 289px; height: 130px; background: var(--crimson); }
  .front-strip { left: 607px; width: 101px; height: 15px; background: var(--white); }
  .front-strip.top { top: 122px; }
  .front-strip.bottom { top: 267px; }
  .front-name {
    position: absolute; left: 78px; top: 170px;
    font-size: 64px; line-height: 74px; color: var(--white); letter-spacing: 1px;
  }
  .partner {
    position: absolute; left: 450px; top: 177px;
    display: flex; align-items: center; gap: 12px;
    color: var(--white); font-size: 26px; line-height: 1;
  }
  .partner-dot { width: 46px; height: 46px; border-radius: 50%; background: var(--white); flex: none; }

  /* Back */
  .back-tab { left: 0; top: 137px; width: 37px; height: 130px; background: var(--navy); }
  .back-band { left: 237px; top: 137px; width: 471px; height: 130px; background: var(--navy); }
  .back-strip { left: 608px; width: 100px; height: 15px; background: var(--crimson); }
  .back-strip.top { top: 122px; }
  .back-strip.bottom { top: 267px; }
  .back-name {
    position: absolute; left: 115px; top: 203px;
    transform: translate(-50%, -50%) rotate(-90deg);
    font-size: 60px; line-height: 60px; color: var(--ink); white-space: nowrap;
  }
  .back-partner {
    position: absolute; left: 192px; top: 203px;
    transform: translate(-50%, -50%) rotate(-90deg);
    font-size: 17px; line-height: 1; color: var(--ink); white-space: nowrap;
  }
  .contact-row { position: absolute; left: 285px; display: flex; align-items: center; gap: 19px; }
  .contact-row.phone { top: 56px; }
  .contact-row.email { top: 300px; }
  .icon-box {
    width: 47px; height: 47px; background: var(--navy);
    display: flex; align-items: center; justify-content: center; flex: none;
  }
  .contact-text { font-size: 22px; color: var(--ink); }
  .social-row {
    position: absolute; left: 283px; top: 180px;
    display: flex; align-items: center;
  }
  .social-chip {
    width: 44px; height: 44px; border-radius: 50%; background: var(--white);
    color: var(--navy); font-size: 12px;
    display: flex; align-items: center; justify-content: center;
    margin-right: 20px;
  }
  .social-handle { font-size: 20px; color: var(--white); margin-left: 2px; }
</style>
</head>
<body>
  <section class="card card-front" aria-label="Card front">
    <div class="block front-tab"></div>
    <div class="block front-panel"></div>
    <div class="block front-strip top"></div>
    <div class="block front-strip bottom"></div>
    <div class="front-name">DJ KESTRO</div>
    <div class="partner"><span class="partner-dot"></span><span>Quietwave Disco</span></div>
  </section>

  <section class="card card-back" aria-label="Card back">
    <div class="block back-tab"></div>
    <div class="block back-band"></div>
    <div class="block back-strip top"></div>
    <div class="block back-strip bottom"></div>
    <div class="back-name">DJ KESTRO</div>
    <div class="back-partner">Quietwave Disco</div>

    <div class="contact-row phone">
      <div class="icon-box">
        <svg width="24" height="24" viewBox="0 0 24 24" aria-hidden="true">
          <path fill="#fff" d="M6.6 10.8a15.2 15.2 0 0 0 6.6 6.6l2.2-2.2a1 1 0 0 1 1-.25 11.4 11.4 0 0 0 3.6.57 1 1 0 0 1 1 1V20a1 1 0 0 1-1 1A17 17 0 0 1 3 4a1 1 0 0 1 1-1h3.5a1 1 0 0 1 1 1c0 1.25.2 2.45.57 3.57a1 1 0 0 1-.25 1z"/>
        </svg>
      </div>
      <span class="contact-text">(555) 314-7720</span>
    </div>

    <div class="social-row">
      <span class="social-chip">Loop</span>
      <span class="social-chip">Pix</span>
      <span class="social-chip">Clip</span>
      <span class="social-handle">@DJKestroBPZ</span>
    </div>

    <div class="contact-row email">
      <div class="icon-box">
        <svg width="32" height="22" viewBox="0 0 32 22" aria-hidden="true">
          <rect x="1" y="1" width="30" height="20" fill="none" stroke="#fff" stroke-width="1.6"/>
          <polyline points="1,1 16,12 31,1" fill="none" stroke="#fff" stroke-width="1.6"/>
          <polyline points="1,21 12,10" fill="none" stroke="#fff" stroke-width="1.2"/>
          <polyline points="31,21 20,10" fill="none" stroke="#fff" stroke-width="1.2"/>
        </svg>
      </div>
      <span class="contact-text">lenny.corbitt@mailvane.net</span>
    </div>
  </section>
</body>
</html>
```